Beatrices Business Card

Looking for business card that is PROFESSIONAL yet has a flair of design. My colors are white with black font. My last name is Halloway so a tiara could be faded in the background OR embossed. I would love my pic to be in a frame with an interesting background/texture. Fonts need to be CLASSY, not cheesy. I need ALL verbiage included but can be on both back and front.

Beatrice Halloway
Real Estate Agent
720-555-0193 bhalloway@velmora.net

Accredited Highland Terrain Advisor
Accredited Premier Dwelling Promotion Advisor
Accredited Settlement Adept

Velmora Keystone
41726 Driftwood Blvd 303-555-014 Each office indepdendly owned and operated

Target Market(s)

Sellers and Buyers. Millennials on up

Industry/Entity Type

Real Estate Agent

Contact Information for Business Card

Beatrice Halloway
Real Estate Agent

Velmora Keystone
41726 Driftwood Blvd 303-555-014
Each office independently owned and operated

Font styles to use
Serif

Colors
f04a50
ffffff
000000

Requirements
Must have
• a classy, fun feel to it. Unique, high end. But it has to look professional and be taken seriously.
Nice to have
• Elegant, classy, fun.
Should not have
• anything cheesy or tacky.

```html
<!DOCTYPE html>
<html lang="en">
<head>
<meta charset="utf-8">
<title>Beatrice Halloway Business Card</title>
<link rel="stylesheet" href="https://fonts.googleapis.com/css2?family=Cinzel:wght@400;700&display=swap">
<style>
  :root {
    --accent: #f04a50;
    --ink: #1a1a1a;
    --muted: #555555;
    --card: #fbfbfa;
    --page: #e9e9e7;
    --gold-a: #e8d9a8;
    --gold-b: #c9a85a;
    --faded-a: #efeee9;
    --faded-b: #e4e2da;
    --photo-a: #b7763f;
    --photo-b: #d2232f;
  }
  * { box-sizing: border-box; margin: 0; padding: 0; }
  html, body { width: 1200px; height: 1000px; overflow: hidden; }
  body {
    background: var(--page);
    font-family: "Cinzel", "Times New Roman", serif;
    color: var(--ink);
    display: flex;
    flex-direction: column;
    align-items: center;
    justify-content: center;
    gap: 32px;
  }
  .card {
    position: relative;
    width: 800px;
    height: 457px;
    background: var(--card);
    border-radius: 22px;
    overflow: hidden;
    box-shadow: 0 6px 18px rgba(0,0,0,0.12);
  }

  /* Back */
  .card-back { display: flex; flex-direction: column; align-items: center; }
  .tiara-art {
    margin-top: 48px;
    width: 300px;
    height: 190px;
    border-radius: 150px 150px 24px 24px;
    background: radial-gradient(ellipse at 50% 40%, var(--gold-a), var(--gold-b) 90%);
    opacity: 0.85;
  }
  .office-name { margin-top: 44px; font-size: 26px; letter-spacing: 1px; }
  .office-address { margin-top: 6px; font-size: 18px; letter-spacing: 0.5px; }
  .office-note { margin-top: 12px; font-size: 12px; letter-spacing: 1px; }

  /* Front */
  .tiara-faded {
    position: absolute;
    left: 410px;
    top: 110px;
    width: 260px;
    height: 185px;
    border-radius: 130px 130px 22px 22px;
    background: radial-gradient(ellipse at 50% 40%, var(--faded-a), var(--faded-b) 90%);
    opacity: 0.75;
  }
  .portrait {
    position: absolute;
    right: 0;
    top: 0;
    width: 330px;
    height: 457px;
    background: linear-gradient(180deg, var(--card) 0%, var(--photo-a) 35%, var(--photo-b) 70%);
  }
  .accent-block {
    position: absolute;
    left: 0;
    top: 178px;
    width: 44px;
    height: 38px;
    background: var(--accent);
  }
  .identity { position: absolute; left: 78px; top: 150px; }
  .first-name { font-size: 40px; font-weight: 700; color: var(--accent); line-height: 1; letter-spacing: 1px; }
  .last-name { font-size: 22px; color: var(--ink); line-height: 1.1; }
  .role { font-size: 14px; color: var(--muted); margin-top: 4px; letter-spacing: 0.5px; }
  .contact { list-style: none; margin-top: 18px; font-size: 17px; }
  .contact li { display: flex; align-items: center; gap: 8px; margin-bottom: 4px; }
  .contact svg { width: 16px; height: 16px; flex: none; }
  .credentials {
    position: absolute;
    left: 78px;
    top: 318px;
    list-style: none;
    font-size: 15px;
    line-height: 1.25;
  }
  .credentials li { position: relative; padding-left: 18px; margin-bottom: 6px; max-width: 360px; }
  .credentials li::before {
    content: "";
    position: absolute;
    left: 0;
    top: 5px;
    width: 8px;
    height: 8px;
    background: var(--accent);
  }
</style>
</head>
<body>
  <section class="card card-back">
    <div class="tiara-art" role="img" aria-label="Gold jewelled tiara illustration"></div>
    <p class="office-name">VELMORA KEYSTONE</p>
    <p class="office-address">41726 DRIFTWOOD BLVD 303-555-014</p>
    <p class="office-note">EACH OFFICE INDEPDENDLY OWNED AND OPERATED</p>
  </section>

  <section class="card card-front">
    <div class="tiara-faded" role="img" aria-label="Faded tiara illustration in the background"></div>
    <div class="portrait" role="img" aria-label="Portrait photo of Beatrice Halloway in a red blouse"></div>
    <div class="accent-block"></div>
    <div class="identity">
      <h1 class="first-name">BEATRICE</h1>
      <p class="last-name">HALLOWAY</p>
      <p class="role">REAL ESTATE AGENT</p>
      <ul class="contact">
        <li>
          <svg viewBox="0 0 16 16" aria-hidden="true"><circle cx="8" cy="8" r="8" fill="var(--accent)"/><path d="M5 4.5l1.6-.4.9 2-1 .8a5 5 0 0 0 2.6 2.6l.8-1 2 .9-.4 1.6c-3.4.3-6.8-3.1-6.5-6.5z" fill="#fff"/></svg>
          720-555-0193
        </li>
        <li>
          <svg viewBox="0 0 16 16" aria-hidden="true"><circle cx="8" cy="8" r="8" fill="var(--accent)"/><rect x="4" y="5" width="8" height="6" fill="#fff"/><path d="M4 5l4 3.3L12 5" stroke="var(--accent)" stroke-width="1" fill="none"/></svg>
          BHALLOWAY@VELMORA.NET
        </li>
      </ul>
    </div>
    <ul class="credentials">
      <li>ACCREDITED HIGHLAND TERRAIN ADVISOR</li>
      <li>ACCREDITED PREMIER DWELLING PROMOTION ADVISOR</li>
      <li>ACCREDITED SETTLEMENT ADEPT</li>
    </ul>
  </section>
</body>
</html>
```